Small, static, 2 page website that promotes 3-6 workshops

This is a microsite for my company that promotes 3 (and later 6) security workshops for developers. The address is going to be codewacht-cursussen.nl so it is very important that the title reads 'Codewacht Cursussen' and the subtitle reads 'voor ontwikkelaars' (means for developers in dutch).

On the frontpage, there will be a small introduction text (about 50 words) about the workshops in general and there should be 3 workshops listed on the frontpage with also a small introduction text. All the workshops are cyber security/hacking related so maybe a small graphic for every workshop would lighten things up.

Then when a visitor clicks a 'more info' button a detail page about that specific workshop with a longer description, a date/location, a 'book now' button and a price should be show.

I have include a quick drawing of what I have in mind for the frontpage, this is not set in stone so you could come up with something else.

I also included my company logo, it should be clear on the site that these workshops are 'Halvard Shield' workshops.

Target Market(s)

Development companies looking for security workshops, the responsible people for those type of workshops are usually security officers, lead developers/managers or developers themselves.

Industry/Entity Type

It Company

Number of Pages Required

2 page

Font styles to use
Sans Serif
Other font styles liked:

Requirements
Must have
• 3 highlighted trainings on the frontpage and a detail page and the title and subtitle as headings on the page.
Nice to have
• I'd really like to have the 3 boxes on the frontpage to have icons or some sort of images. The first 3 workshops that are going to be on the page are:
• - Security awareness for developers
• - Web application security from a hackers perspective
• - Penetrationtesting for developers

```html
<!DOCTYPE html>
<html lang="nl">
<head>
<meta charset="utf-8">
<title>Codewacht Cursussen – Halvard Shield</title>
<link href="https://fonts.googleapis.com/css2?family=Roboto:wght@300;400;500;700&family=Open+Sans:wght@400;600&display=swap" rel="stylesheet">
<style>
:root{
  --navy:#173a6b;
  --navy-dark:#0f2a52;
  --text:#6f6f6f;
  --heading:#444;
  --line:#d9dde3;
  --panel:#f4f6f9;
  --white:#fff;
  --footer-bar:#6b6b6d;
  --cyan:#4fd0ff;
}
*{box-sizing:border-box;margin:0;padding:0}
html,body{width:770px;height:1200px;overflow:hidden;background:var(--white)}
body{position:relative;font-family:"Roboto",Arial,sans-serif;color:var(--text)}
.abs{position:absolute}

/* header */
.site-header{left:0;top:0;width:770px;height:58px;background:var(--white)}
.brand{display:flex;align-items:center;gap:8px;left:55px;top:16px}
.brand-mark{width:26px;height:26px;background:var(--navy);border-radius:50%}
.brand-name{font-size:17px;font-weight:500;color:var(--navy);letter-spacing:1px;text-transform:uppercase}
.main-nav{display:flex;gap:24px;right:55px;top:27px;font-size:8px;font-weight:500;text-transform:uppercase}
.main-nav a{color:#6a4a2d;text-decoration:none}
.main-nav a.active{color:var(--navy)}

/* hero */
.hero{left:0;top:58px;width:770px;height:311px;background:linear-gradient(100deg,#0b1c3c 0%,#0d2f63 40%,#1275c4 70%,#39c8f5 90%,#7fe3ff 100%)}
.hero-copy{left:55px;top:91px;width:270px;color:var(--white)}
.hero-title{font-size:17px;font-weight:500;text-transform:uppercase;letter-spacing:.2px}
.hero-sub{font-size:22px;font-weight:300;text-transform:uppercase;margin-top:9px}
.hero-text{font-size:7.4px;line-height:16px;margin-top:12px}
.btn-ghost{display:inline-flex;align-items:center;justify-content:center;border:1px solid var(--white);color:var(--white);font-size:9px;font-weight:500;width:88px;height:27px;border-radius:2px;margin-top:17px;text-transform:uppercase}
.hero-dots{left:55px;top:345px;display:flex;gap:4px}
.hero-dots span{width:10px;height:10px;border:1.3px solid var(--white);border-radius:50%}
.hero-dots span.on{border-color:var(--cyan)}

/* intro */
.intro{left:0;top:392px;width:770px;text-align:center}
.section-title{font-size:13px;font-weight:700;color:var(--navy);text-transform:uppercase}
.intro p{width:430px;margin:13px auto 0;font-size:7.2px;line-height:15.4px}

/* trainings */
.training{top:489px;width:200px;text-align:center}
.training-icon{width:81px;height:81px;margin:0 auto;border-radius:50%;background:var(--navy);border:2px solid var(--white);box-shadow:0 0 0 1.5px var(--navy);display:flex;align-items:center;justify-content:center}
.training h3{font-size:11px;font-weight:500;color:var(--navy-dark);margin-top:11px;text-transform:uppercase}
.training p{font-size:7.2px;line-height:15.4px;margin-top:9px}
.btn-outline{display:inline-flex;align-items:center;justify-content:center;border:1px solid var(--navy);color:var(--navy);font-size:9.5px;font-weight:500;width:80px;height:25px;border-radius:2px;text-transform:uppercase;background:var(--white)}
.training .btn-outline{margin-top:14px}

/* info panel */
.info-panel{left:0;top:717px;width:770px;height:273px;background:var(--panel)}
.col{top:742px;width:206px}
.col h2{font-size:12.5px;font-weight:700;color:var(--navy);text-transform:uppercase}
.col p{font-size:7.2px;line-height:15.4px}
.news-photo{width:194px;height:111px;margin-top:17px;background:linear-gradient(135deg,#5c7a3a,#2f4d23 50%,#1a2b16)}
.field{width:204px;height:23px;background:var(--white);border:1px solid var(--line);font-size:7px;color:#888;padding:7px 8px;margin-top:4px}
.field.tall{height:39px}

/* footer */
.footer-brand{left:55px;top:1061px}
.footer-col{top:1017px}
.footer-col h4{font-size:10px;font-weight:400;color:#444;text-transform:uppercase;letter-spacing:.2px}
.contact-list{list-style:none;margin-top:14px;font-size:7.3px}
.contact-list li{display:flex;gap:7px;align-items:flex-start;margin-bottom:9px}
.contact-list svg{flex:none;margin-top:1px}
.contact-list a{color:var(--text)}
.news-note{font-family:"Open Sans",Arial,sans-serif;font-size:7px;line-height:13.5px;margin-top:14px;width:140px}
.email-field{width:136px;height:21px;border:1px solid var(--line);font-size:7.5px;color:#555;padding:6px 9px;margin-top:9px}
.btn-subscribe{display:inline-flex;align-items:center;justify-content:center;background:var(--navy);color:var(--white);font-size:6.5px;font-weight:500;width:52px;height:18px;margin-top:7px;text-transform:uppercase}
.follow-note{font-family:"Open Sans",Arial,sans-serif;font-size:6.5px;line-height:12px;margin-top:14px;width:125px}
.socials{display:flex;gap:4px;margin-top:12px}
.socials span{width:23px;height:23px;border:1px solid #aaa;border-radius:50%}
.footer-bar{left:0;top:1132px;width:770px;height:68px;background:var(--footer-bar);color:var(--white);font-size:7.5px;text-align:center;padding-top:39px}
</style>
</head>
<body>

<header class="site-header abs">
  <div class="brand abs"><span class="brand-mark"></span><span class="brand-name">Halvard Shield</span></div>
  <nav class="main-nav abs">
    <a class="active" href="#">Home</a><a href="#">About us</a><a href="#">Services</a><a href="#">Offer</a><a href="#">News</a><a href="#">Contact us</a>
  </nav>
</header>

<section class="hero abs" role="img" aria-label="Blue digital circuit background with a glowing padlock"></section>
<div class="hero-copy abs">
  <h1 class="hero-title">Codewacht Cursussen</h1>
  <div class="hero-sub">voor ontwikkelaars</div>
  <p class="hero-text">From the first moment you have your own cybersecurity expert who can advise his knowledge and years of experience in the right way on the steps to take to achieve the detsired level of security</p>
  <span class="btn-ghost">Read more</span>
</div>
<div class="hero-dots abs"><span></span><span class="on"></span><span></span><span></span></div>

<section class="intro abs">
  <h2 class="section-title">Welcome to Halvard Shield</h2>
  <p>From the first moment you have your own cybersecurity expert who can advise his knowledge and years of experience in the right way on the steps to take to achieve the detsired level of security within your organization. So you sit flush with the right person at the table and have already benefited from the first call.</p>
</section>

<article class="training abs" style="left:57px">
  <div class="training-icon">
    <svg width="34" height="40" viewBox="0 0 34 40" fill="none" stroke="#fff" stroke-width="2.4"><path d="M9 18V11a8 8 0 0 1 16 0v7"/><rect x="4" y="18" width="26" height="19" rx="2"/><circle cx="17" cy="26" r="2.4" fill="#fff" stroke="none"/><path d="M17 27v5"/></svg>
  </div>
  <h3>Training 1</h3>
  <p>From the first moment you have your own cyberse-<br>curity expert who can advise his knowledge and yea<br>have your own experience in the right</p>
  <span class="btn-outline">More info</span>
</article>

<article class="training abs" style="left:282px">
  <div class="training-icon">
    <svg width="42" height="34" viewBox="0 0 42 34" fill="none" stroke="#fff" stroke-width="2.4"><path d="M8 10l8 8-8 8"/><path d="M20 27h14"/><rect x="2" y="2" width="38" height="30" rx="3"/></svg>
  </div>
  <h3>Training 2</h3>
  <p>From the first moment you have your own cybersecu-<br>rity expert who can advise his knowledge and yea<br>have your own experience in the right</p>
  <span class="btn-outline">More info</span>
</article>

<article class="training abs" style="left:506px">
  <div class="training-icon">
    <svg width="42" height="38" viewBox="0 0 42 38" fill="none" stroke="#fff" stroke-width="2.4"><rect x="2" y="2" width="38" height="26" rx="2"/><path d="M21 28v5M13 35h16"/><circle cx="21" cy="15" r="6"/><path d="M25 19l5 5"/></svg>
  </div>
  <h3>Training 3</h3>
  <p>From the first moment you have your own cybersecu-<br>rity expert who can advise his knowledge and yea<br>have your own experience in the right</p>
  <span class="btn-outline">More info</span>
</article>

<section class="info-panel abs"></section>

<div class="col abs" style="left:55px">
  <h2>About us</h2>
  <p style="margin-top:15px">From the first moment you have your own cybersecurity expert who can advise his knowledge and years of expe-rience in the right&nbsp; From the first moment you have your own cybersecurity expert who can advise his knowledge and years of experience in the right</p>
  <p style="margin-top:15px">From the first moment you have your own cybersecurity expert who can advise his knowledge and years of expe-rience in the right&nbsp; From the first</p>
  <span class="btn-outline" style="margin-top:24px">Read more</span>
</div>

<div class="col abs" style="left:276px">
  <h2>Latest news</h2>
  <div class="news-photo" role="img" aria-label="Hooded figure working on a laptop over a green circuit board"></div>
  <p style="margin-top:10px">From the first moment you have your own cyberse-<br>curity expert who can advise his</p>
  <span class="btn-outline" style="margin-top:12px">Read more</span>
</div>

<div class="col abs" style="left:496px;width:220px">
  <h2>Quick contact</h2>
  <p style="margin-top:10px">From the first moment you have your own cybersecurity expert who can advise his knowledge</p>
  <div style="margin-top:8px">
    <div class="field">Name *</div>
    <div class="field">Phone *</div>
    <div class="field">E Mail *</div>
    <div class="field tall">Massage *</div>
  </div>
  <span class="btn-outline" style="margin-top:9px;width:64px">Send</span>
</div>

<div class="brand footer-brand abs" style="display:flex;align-items:center;gap:8px"><span class="brand-mark"></span><span class="brand-name">Halvard Shield</span></div>

<div class="footer-col abs" style="left:229px">
  <h4>Contact us</h4>
  <ul class="contact-list">
    <li><svg width="9" height="8" viewBox="0 0 9 8" fill="#999"><path d="M0 2q4.5-3 9 0v1H7V2H2v1H0z"/><rect x="1" y="4" width="7" height="4" rx="1"/></svg>Phone - 000-121-1231</li>
    <li><svg width="9" height="8" viewBox="0 0 9 8" fill="#999"><rect x="2" y="0" width="5" height="3"/><rect x="0" y="3" width="9" height="5" rx="1"/></svg>Fax - 000-121-1231</li>
    <li><svg width="9" height="7" viewBox="0 0 9 7" fill="#999"><rect width="9" height="7"/><path d="M0 0l4.5 4L9 0" stroke="#fff" fill="none"/></svg><a href="#">Email : info@halvardshield.nl</a></li>
    <li><svg width="7" height="10" viewBox="0 0 7 10" fill="none" stroke="#999" stroke-width="1.3"><path d="M3.5 9.5S.7 6 .7 3.6a2.8 2.8 0 0 1 5.6 0C6.3 6 3.5 9.5 3.5 9.5z"/></svg><span># 235 Lorem Ipsum Dummy<br>Lorem Ippaum</span></li>
  </ul>
</div>

<div class="footer-col abs" style="left:401px">
  <h4>Newsletter</h4>
  <p class="news-note">Register Your email address to get information abount us</p>
  <div class="email-field">Email Address</div>
  <span class="btn-subscribe">Subscribe</span>
</div>

<div class="footer-col abs" style="left:564px">
  <h4>Follow us</h4>
  <p class="follow-note">Lorem ipsum dolor sit amet, conse ctetur adipiscing elit. Nulla in purus nibh. Donec ornare</p>
  <div class="socials"><span></span><span></span><span></span><span></span><span></span></div>
</div>

<footer class="footer-bar abs">© Copyright 2016 Halvard Shield.All Rights Reserved</footer>

</body>
</html>
```